Velmora - 3D medical animations and high end visual content

Our company creates high end visual content and animations for medical global companies.
Our website - www.velmora-studio.example
We would like to have an amazing business card for our CEO that he can use in the following exhebitions he is going to attend.
It is very important that the design will be memorable and diffrent. It has to reflect our brand design (you can have it from our website)
We would like to transmit innovation, prestige, luxury, aesthetics.
The card has to be Double Sided

Target Market(s)

Marketing managers in medical global companys

Industry/Entity Type

It Company

Contact Information for Business Card

Requirements
Nice to have
• It is very important that the design will be memorable and diffrent. It has to reflect our brand design (you can have it from our website)

```html
<!DOCTYPE html>
<html lang="en">
<head>
<meta charset="utf-8">
<title>Velmora — Business Card</title>
<link href="https://fonts.googleapis.com/css2?family=Montserrat:wght@400;500;700&family=Open+Sans:wght@300;400;600;700&display=swap" rel="stylesheet">
<style>
  :root {
    --backdrop: #a9a8a9;
    --card-black: #141414;
    --card-white: #ffffff;
    --ink-white: #f2f2f2;
    --ink-grey: #c9c9c9;
    --ink-black: #111111;
    --accent-teal: #1c9ab3;
    --rule-grey: #8a8a8a;
  }
  * { margin: 0; padding: 0; box-sizing: border-box; }
  html, body { width: 1200px; height: 1000px; overflow: hidden; }
  body {
    background: var(--backdrop);
    font-family: "Open Sans", Arial, sans-serif;
    position: relative;
  }
  .card {
    position: absolute;
    left: 300px;
    width: 600px;
    height: 340px;
    border-radius: 26px;
    overflow: hidden;
    background: var(--card-black);
  }
  .card--front { top: 110px; }
  .card--back { top: 550px; display: flex; }

  /* Front */
  .front-wordmark {
    position: absolute;
    left: 0; right: 0; top: 128px;
    text-align: center;
  }
  .front-wordmark__name {
    font-family: "Montserrat", Arial, sans-serif;
    font-weight: 500;
    font-size: 56px;
    letter-spacing: 4px;
    color: var(--ink-white);
    line-height: 1;
  }
  .front-wordmark__rule {
    width: 360px;
    height: 1px;
    margin: 16px auto 0;
    background: var(--ink-white);
    opacity: 0.8;
  }

  /* Back */
  .back-strip {
    width: 172px;
    height: 100%;
    background: var(--card-white);
    position: relative;
  }
  .back-strip__name {
    position: absolute;
    left: 50%; top: 50%;
    transform: translate(-50%, -50%) rotate(-90deg);
    font-family: "Montserrat", Arial, sans-serif;
    font-weight: 500;
    font-size: 48px;
    letter-spacing: 4px;
    color: var(--ink-black);
    white-space: nowrap;
  }
  .back-strip__rule {
    position: absolute;
    left: 124px; top: 36px; bottom: 36px;
    width: 1px;
    background: var(--rule-grey);
  }
  .back-info {
    flex: 1;
    padding: 78px 0 0 72px;
    color: var(--ink-white);
  }
  .person-name {
    font-weight: 700;
    font-size: 22px;
    letter-spacing: 0.5px;
    line-height: 1.1;
  }
  .person-name__last { color: var(--accent-teal); }
  .person-role {
    font-weight: 600;
    font-size: 16px;
    margin-top: 4px;
  }
  .contact-list {
    list-style: none;
    margin-top: 34px;
  }
  .contact-list li {
    display: flex;
    align-items: center;
    gap: 14px;
    font-weight: 300;
    font-size: 14px;
    color: var(--ink-grey);
    height: 22px;
  }
  .contact-icon { width: 13px; height: 13px; fill: var(--accent-teal); flex: none; }
  .contact-domain { color: var(--accent-teal); }
</style>
</head>
<body>

<section class="card card--front" aria-label="Card front">
  <div class="front-wordmark">
    <div class="front-wordmark__name">VELMORA</div>
    <div class="front-wordmark__rule"></div>
  </div>
</section>

<section class="card card--back" aria-label="Card back">
  <div class="back-strip">
    <div class="back-strip__name">VELMORA</div>
    <div class="back-strip__rule"></div>
  </div>
  <div class="back-info">
    <div class="person-name">LIOR <span class="person-name__last">KATAN</span></div>
    <div class="person-role">FOUNDER &amp; CEO</div>
    <ul class="contact-list">
      <li>
        <svg class="contact-icon" viewBox="0 0 16 16" aria-hidden="true"><path d="M2 5c0-2 2-3 6-3s6 1 6 3v1h-3V5H5v1H2z M4 7h8l2 6H2z"/></svg>
        +972-50-4412783
      </li>
      <li>
        <svg class="contact-icon" viewBox="0 0 16 16" aria-hidden="true"><path d="M4 1l3 3-2 2c1 2 3 4 5 5l2-2 3 3-2 3C7 15 1 9 1 3z"/></svg>
        +972-73-2265410
      </li>
      <li>
        <svg class="contact-icon" viewBox="0 0 16 16" aria-hidden="true"><path d="M1 3h14v10H1z M2 4l6 5 6-5" fill="none" stroke="#1c9ab3" stroke-width="1.6"/><path d="M1 3h14v10H1z"/><path d="M1.5 4l6.5 5 6.5-5" fill="none" stroke="#141414" stroke-width="1.4"/></svg>
        lior@velmora-studio.example
      </li>
      <li>
        <svg class="contact-icon" viewBox="0 0 16 16" aria-hidden="true"><circle cx="8" cy="8" r="7"/><path d="M1 8h14M8 1c-3 3-3 11 0 14M8 1c3 3 3 11 0 14" fill="none" stroke="#141414" stroke-width="1"/></svg>
        <span>www.<span class="contact-domain">velmora-studio</span>.example</span>
      </li>
    </ul>
  </div>
</section>

</body>
</html>
```